Tranquil Glide Door Product info

Need a catalog designed. 4 -6 pages
We are a commercial sliding door company.
Primary product is a barn door
35 STC Rating (sound rating)
see our web pages listed below
www.tranquilglidedoor-example.com
www.quickrailstock-example.com
Our product is gaining huge strides throughout the medical and hospitality sectors.
this is a 4- 6 page catalogue / brochure . Our product is currently used in many places but we also are creating new markets in the office space.
Updates

Target Market(s)

Commercial Architects , designers , Contractors .
Hospitals , high end hotels , Commercial building planners

Industry/Entity Type

Construction Company

Font styles to use
Serif

Requirements
Must have
• Selling points as to why our product is superior, good flow from concept to end. catch the eye of a designer . technical info . info on sound rating , Good photos, will provide better photos.
Nice to have
• see website from meridan doors and see ideas
Should not have
• too much writing

```html
<!DOCTYPE html>
<html lang="en">
<head>
<meta charset="utf-8">
<title>Tranquil Glide Door – Catalogue Cover</title>
<link href="https://fonts.googleapis.com/css2?family=Oswald:wght@500&family=Marcellus&display=swap" rel="stylesheet">
<style>
  :root {
    --stage: #000000;
    --paper: #ffffff;
    --headline: #ffffff;
    --brand: #2f3a48;
    --brand-accent: #2b6f93;
    --tint-blue: #56b4ec;
    --tint-sand: #d9c6bd;
  }
  html, body {
    margin: 0;
    width: 1200px;
    height: 502px;
    overflow: hidden;
    background: var(--stage);
  }
  .canvas {
    position: relative;
    width: 1200px;
    height: 502px;
  }
  .catalogue-cover {
    position: absolute;
    left: 420px;
    top: 17px;
    width: 361px;
    height: 467px;
    display: block;
  }
  .cover-headline {
    font-family: "Oswald", "Arial Narrow", sans-serif;
    font-weight: 500;
    font-size: 10.6px;
    fill: var(--headline);
    letter-spacing: 0.1px;
  }
  .cover-url {
    font-family: "Oswald", "Arial Narrow", sans-serif;
    font-weight: 500;
    font-size: 10.4px;
    fill: var(--headline);
  }
  .brand-name {
    font-family: "Marcellus", Georgia, serif;
    font-size: 18px;
    fill: var(--brand);
  }
  .brand-tagline {
    font-family: "Marcellus", Georgia, serif;
    font-size: 9.5px;
    fill: var(--brand);
    letter-spacing: 0.4px;
  }
</style>
</head>
<body>
<main class="canvas">
  <svg class="catalogue-cover" viewBox="0 0 433 560" xmlns="http://www.w3.org/2000/svg">
    <defs>
      <linearGradient id="hallway-tones" x1="0" y1="0" x2="0.6" y2="1">
        <stop offset="0" stop-color="#d9d6cf"/>
        <stop offset="0.35" stop-color="#a9a59d"/>
        <stop offset="0.6" stop-color="#4a4a4f"/>
        <stop offset="1" stop-color="#1e2026"/>
      </linearGradient>
      <clipPath id="photo-shape">
        <polygon points="9,16 421,16 421,548 208,548 9,304"/>
      </clipPath>
    </defs>

    <rect class="cover-paper" width="433" height="560" fill="var(--paper)"/>

    <g clip-path="url(#photo-shape)">
      <rect class="cover-photo" x="9" y="16" width="412" height="532" fill="url(#hallway-tones)"
            role="img" aria-label="Photo of a medical office corridor with wood and glass sliding barn doors"/>
      <g class="geometric-tints">
        <polygon points="9,16 180,16 9,190" fill="var(--tint-sand)" opacity="0.45"/>
        <polygon points="9,120 150,16 300,16 9,330" fill="var(--tint-blue)" opacity="0.35"/>
        <polygon points="60,330 230,120 330,330 200,548" fill="var(--tint-blue)" opacity="0.35"/>
        <polygon points="200,16 330,16 220,250" fill="var(--tint-blue)" opacity="0.25"/>
        <polygon points="230,420 421,300 421,548 250,548" fill="var(--tint-blue)" opacity="0.3"/>
      </g>
    </g>

    <text class="cover-headline" x="216" y="34" text-anchor="middle">MODERN SLIDING DOOR SYSTEM FOR HOSPITALITY, MEDICAL, ASSISTED LIVING AND OFFICE</text>
    <text class="cover-url" x="222" y="541" textLength="190" lengthAdjust="spacingAndGlyphs">WWW.TRANQUILGLIDEDOOR-EXAMPLE.COM</text>

    <g class="brand-lockup">
      <rect x="76" y="432" width="26" height="26" fill="var(--brand-accent)"/>
      <text class="brand-name" x="89" y="505" text-anchor="middle">Tranquil Glide</text>
      <text class="brand-tagline" x="89" y="528" text-anchor="middle">Sliding Door Systems</text>
    </g>
  </svg>
</main>
</body>
</html>
```